**** Business card design for VoltaNode ****

For my ICT company VoltaNode I need I need a business card design.

We design, build and host web-applications and we have our own CMS product.

Some good examples are attached.

The information should be:
Joris Tielenburg
Managing director
E: j.tielenburg@voltanode-example.nl
M: +31(0)6 57218064
T: +31(0)40 7249305
W: www.voltanode-example.nl

Address:
Berend Vlootweg 27
5612 KT Eindhoven

Industry/Entity Type

Business

Requirements
Must have
• - Use logo (see attachments)
- Double sided
- Distinctive
Nice to have
• - Place for a statement on the back-side: "Designed with knowledge, built with passion"
- HTML code (or Wordpress)
- Dark (black or dark-gray) side
- Small simple images for telephone, e-mail en Url.
- QR code (only if not disturbing), not required, just an option

```html
<!DOCTYPE html>
<html lang="en">
<head>
<meta charset="utf-8">
<title>VoltaNode business card</title>
<link rel="stylesheet" href="https://fonts.googleapis.com/css2?family=Questrial&display=swap">
<style>
  :root {
    --frame: #000000;
    --paper: #ffffff;
    --brand-blue: #1ab0e6;
    --brand-grey: #5f6b70;
    --on-blue: #ffffff;
  }
  html, body {
    margin: 0;
    padding: 0;
    width: 1015px;
    height: 1200px;
    overflow: hidden;
    background: var(--frame);
    font-family: "Questrial", "Century Gothic", sans-serif;
  }
  .canvas {
    position: relative;
    width: 1015px;
    height: 1200px;
    background: var(--frame);
  }
  .card {
    position: absolute;
    left: 10px;
    width: 996px;
    background: var(--paper);
    overflow: hidden;
  }
  .card--front { top: 10px; height: 584px; }
  .card--back  { top: 605px; height: 585px; }

  .brand {
    position: absolute;
    left: 190px;
    top: 215px;
    display: flex;
    align-items: center;
    gap: 34px;
  }
  .brand__dot {
    width: 150px;
    height: 150px;
    border-radius: 50%;
    background: var(--brand-blue);
  }
  .brand__name {
    font-size: 86px;
    color: var(--brand-grey);
    letter-spacing: 1px;
    line-height: 1;
  }

  .back__panel {
    position: absolute;
    left: 496px;
    top: 0;
    width: 500px;
    height: 100%;
    background: var(--brand-blue);
  }
  .person__role {
    position: absolute;
    left: 104px;
    top: 122px;
    font-size: 25px;
    color: var(--brand-blue);
    margin: 0;
  }
  .person__name {
    position: absolute;
    left: 242px;
    top: 150px;
    margin: 0;
    font-size: 43px;
    font-weight: 400;
    white-space: nowrap;
    background-image: linear-gradient(to right, var(--brand-blue) 254px, var(--on-blue) 254px);
    -webkit-background-clip: text;
    background-clip: text;
    color: transparent;
  }
  .contact {
    position: absolute;
    left: 543px;
    top: 305px;
    margin: 0;
    padding: 0;
    list-style: none;
    color: var(--on-blue);
    font-size: 24px;
    line-height: 34px;
    white-space: nowrap;
  }
</style>
</head>
<body>
<div class="canvas">
  <section class="card card--front">
    <div class="brand">
      <span class="brand__dot" aria-hidden="true"></span>
      <span class="brand__name">VoltaNode</span>
    </div>
  </section>

  <section class="card card--back">
    <div class="back__panel"></div>
    <p class="person__role">Managing director</p>
    <h1 class="person__name">Joris Tielenburg</h1>
    <ul class="contact">
      <li>E: j.tielenburg@voltanode-example.nl</li>
      <li>M: +31(0)6 57218064</li>
      <li>T: +31(0)40 7249305</li>
      <li>W: www.voltanode-example.nl</li>
    </ul>
  </section>
</div>
</body>
</html>
```